Klappkarte Kundenanschreiben
Zielgruppe
Kunden, die eine Nähmaschine bei uns gekauft haben, erhalten eine Karte mit einem Nadelset
Aufgabenstellung
Anlass für Klappkarte - siehe Datenanhang
Gestaltung einer Klappkarte DIN lang Querformat.
Außenseiten aufgeklappt:
Linke Hälfte - Anschriftenfeld links (für Fensterkuvert DL)
Rechte Hälfte - Grafik / Foto gestaltet (Motiv passend zum Text (Anlass) s. Datenanhang)
Innenseite aufgeklappt:
Linke Hälfe - hier wird eine Visitenkarten sowie ein Nadelset aufgeklebt
Rechte Hälfte - Text (s. Datenanhang)

```html
<!DOCTYPE html>
<html lang="de">
<head>
<meta charset="utf-8">
<title>Klappkarte Kundenanschreiben – Nähmaschine</title>
<link rel="stylesheet" href="https://fonts.googleapis.com/css2?family=Open+Sans:wght@400;600;700;800&display=swap">
<style>
  :root {
    --orange: #e8940f;
    --purple: #5b2d86;
    --brown: #4a2a12;
    --text: #5a5a5a;
    --paper: #ffffff;
    --stage: #ecebe8;
    --photo-light: #eef0f2;
    --photo-mid: #cfd3d8;
    --photo-dark: #a9aeb5;
  }
  * { box-sizing: border-box; margin: 0; padding: 0; }
  html, body { width: 722px; height: 1200px; overflow: hidden; }
  body {
    background: var(--stage);
    font-family: "Open Sans", Arial, sans-serif;
    color: var(--text);
    position: relative;
  }
  .sheet { position: absolute; background: var(--paper); box-shadow: 0 6px 18px rgba(0,0,0,.18); }
  .cover { left: 121px; top: 70px; width: 480px; height: 300px; }
  .spread { left: 21px; width: 680px; height: 212px; display: flex; }
  .spread--inside { top: 480px; }
  .spread--outside { top: 850px; }
  .panel { position: relative; width: 340px; height: 212px; overflow: hidden; }
  .panel + .panel { border-left: 1px solid #e4e4e4; }
  .panel svg, .cover svg { position: absolute; inset: 0; width: 100%; height: 100%; display: block; }

  .letter { position: absolute; left: 18px; top: 56px; width: 250px; font-size: 5.6px; line-height: 1.45; }
  .letter__title { font-size: 9px; font-weight: 800; color: var(--purple); letter-spacing: .2px; }
  .letter__title span { color: var(--orange); }
  .letter__lead { font-weight: 700; color: #444; margin-bottom: 6px; }
  .letter p { margin-bottom: 4px; }
  .letter__wish { color: var(--orange); font-weight: 600; margin-top: 6px; }
  .signatures { display: flex; gap: 30px; margin-top: 6px; }
  .signatures strong { display: block; font-weight: 700; }
  .sig--studio strong { color: var(--purple); }
  .sig--cafe strong { color: var(--orange); }

  .brands { position: absolute; right: 12px; bottom: 40px; display: flex; flex-direction: column; align-items: flex-end; gap: 5px; }
  .brand { display: flex; align-items: center; gap: 4px; font-weight: 700; font-size: 8px; }
  .brand--studio { color: var(--purple); }
  .brand--cafe { color: var(--brown); }
  .brand__mark { width: 8px; height: 8px; background: var(--orange); }
</style>
</head>
<body>

<!-- Titelseite -->
<div class="sheet cover">
  <svg viewBox="0 0 480 300">
    <defs>
      <linearGradient id="photoTone" x1="0" y1="0" x2="1" y2="1">
        <stop offset="0" stop-color="var(--photo-dark)"/>
        <stop offset=".45" stop-color="var(--photo-light)"/>
        <stop offset="1" stop-color="var(--photo-mid)"/>
      </linearGradient>
      <g id="frontArt">
        <rect width="480" height="300" fill="url(#photoTone)" role="img" aria-label="Foto: Nähfuß einer Nähmaschine mit gelber und bunten Garnrollen"/>
        <path d="M0 0H330C200 20 60 80 0 150Z" fill="var(--orange)"/>
        <path d="M0 150C60 80 200 20 330 0H350C215 25 70 88 0 162Z" fill="var(--purple)"/>
        <path d="M0 134C60 68 190 12 300 0" fill="none" stroke="#fff" stroke-width="1.2" stroke-dasharray="5 4"/>
        <path d="M480 108C440 200 330 268 130 300H150C330 275 440 210 480 120Z" fill="var(--purple)"/>
        <path d="M480 120C440 210 330 275 150 300H480Z" fill="var(--paper)"/>
        <path d="M300 8H385V115L342.5 100L300 115Z" fill="var(--orange)"/>
        <path d="M305 13H380V107L342.5 94L305 107Z" fill="none" stroke="#fff" stroke-width="1" stroke-dasharray="4 3"/>
        <rect x="288" y="18" width="60" height="22" rx="11" fill="var(--purple)" role="img" aria-label="Handschrift „lieben“ mit Herz"/>
        <text x="342.5" y="62" text-anchor="middle" fill="#fff" font-family="Open Sans, sans-serif" font-weight="800" font-size="15">GLÜCK-</text>
        <text x="342.5" y="80" text-anchor="middle" fill="#fff" font-family="Open Sans, sans-serif" font-weight="800" font-size="15">WUNSCH!</text>
        <rect x="456" y="258" width="9" height="9" fill="var(--orange)"/>
        <text x="450" y="266" text-anchor="end" fill="var(--brown)" font-family="Open Sans, sans-serif" font-weight="700" font-size="10">Stichpunkt Café</text>
        <text x="465" y="286" text-anchor="end" fill="var(--purple)" font-family="Open Sans, sans-serif" font-weight="700" font-size="12">Nähwerk Studio</text>
      </g>
    </defs>
    <use href="#frontArt"/>
  </svg>
</div>

<!-- Innenseite aufgeklappt -->
<div class="sheet spread spread--inside">
  <div class="panel panel--mount">
    <svg viewBox="0 0 340 212">
      <path d="M0 0H150C95 40 35 100 0 150Z" fill="var(--orange)"/>
      <path d="M0 150C35 100 95 40 150 0H162C105 42 40 104 0 160Z" fill="var(--purple)"/>
      <path d="M0 136C35 88 90 36 136 0" fill="none" stroke="#fff" stroke-width="1" stroke-dasharray="4 3"/>
      <path d="M340 70C300 140 220 190 150 212H165C235 190 312 140 340 84Z" fill="var(--purple)"/>
      <path d="M340 92C315 142 250 186 180 212" fill="none" stroke="var(--orange)" stroke-width="1" stroke-dasharray="4 3"/>
    </svg>
  </div>
  <div class="panel panel--letter">
    <svg viewBox="0 0 340 212">
      <path d="M150 0H340V46C290 24 225 8 150 0Z" fill="var(--orange)"/>
      <path d="M138 0C225 8 290 24 340 46V54C288 30 220 12 126 0Z" fill="var(--purple)"/>
      <path d="M215 3C265 10 305 22 340 36" fill="none" stroke="#fff" stroke-width="1" stroke-dasharray="4 3"/>
    </svg>
    <div class="letter">
      <div class="letter__title">HERZLICHEN <span>GLÜCKWUNSCH!</span></div>
      <div class="letter__lead">Seit einem halben Jahr sind Sie und Ihre Nähmaschine ein starkes Team!</div>
      <p>Bestimmt haben Sie schon viele kreative Projekte verwirklicht und „die Nadel zum Glühen gebracht“.</p>
      <p>Machen Sie weiter so! Mit diesem neuen Nadelsatz können Sie das nächste Projekt (Vorhaben) in Angriff nehmen.</p>
      <p class="letter__wish">Wir wünschen Ihnen viel Spaß und Freude mit Ihrer Nähmaschine.</p>
      <p>Ihre Partner, wenn es ums Nähen geht!</p>
      <div class="signatures">
        <div class="sig--studio"><strong>Nähwerk Studio</strong>Lena Borchardt<br>Waldbach</div>
        <div class="sig--cafe"><strong>Stichpunkt Café</strong>Lindenau</div>
      </div>
    </div>
    <div class="brands">
      <div class="brand brand--cafe"><span>Stichpunkt Café</span><span class="brand__mark"></span></div>
      <div class="brand brand--studio">Nähwerk Studio</div>
    </div>
  </div>
</div>

<!-- Außenseite aufgeklappt -->
<div class="sheet spread spread--outside">
  <div class="panel panel--address">
    <svg viewBox="0 0 340 212">
      <defs>
        <linearGradient id="photoToneBack" x1="0" y1="0" x2="1" y2="1">
          <stop offset="0" stop-color="var(--photo-mid)"/>
          <stop offset=".5" stop-color="var(--photo-light)"/>
          <stop offset="1" stop-color="var(--photo-dark)"/>
        </linearGradient>
      </defs>
      <rect width="340" height="212" fill="url(#photoToneBack)" role="img" aria-label="Foto: Nähmaschine mit gelber und farbigen Garnrollen"/>
      <path d="M340 0H120C180 20 250 50 340 56Z" fill="var(--paper)"/>
      <path d="M120 0C200 30 270 60 340 62V48C270 44 220 30 160 0Z" fill="var(--orange)"/>
      <path d="M110 0C190 32 265 64 340 68V62C270 60 200 30 120 0Z" fill="var(--purple)"/>
      <path d="M160 8C220 30 280 46 340 54" fill="none" stroke="#fff" stroke-width="1" stroke-dasharray="4 3"/>
      <rect x="22" y="112" width="170" height="80" rx="8" fill="var(--paper)" stroke="var(--purple)" stroke-width="1" stroke-dasharray="3 3" aria-label="Anschriftenfeld"/>
    </svg>
  </div>
  <div class="panel panel--front">
    <svg viewBox="0 0 480 300" preserveAspectRatio="none">
      <use href="#frontArt"/>
    </svg>
  </div>
</div>

</body>
</html>
```